Venlow Vaults -responsive, bootstrap website design

Looking to build a responsive service website.

Logo and pictures have been provided.

PLEASE REVIEW ATTACHED DESIGN STYLE GUIDES & CLIENT CREATIVE BRIEF FOR OUR REQUIREMENT. THANK YOU AND GOOD LUCK!
Updates

Industry/Entity Type

Build

```html
<!DOCTYPE html>
<html lang="en">
<head>
<meta charset="utf-8">
<title>Venlow Vaults</title>
<link href="https://fonts.googleapis.com/css2?family=Open+Sans:wght@300;400;600;700&family=Roboto+Slab:wght@700&display=swap" rel="stylesheet">
<style>
:root{
  --bar:#3a3a3a;
  --footer:#333333;
  --footer-line:#262626;
  --ink:#222;
  --muted:#555;
  --footer-text:#a9a9a9;
  --accent:#8e1b1b;
  --page:#ececec;
  --white:#fff;
  --btn:#3c3c3c;
}
*{margin:0;padding:0;box-sizing:border-box}
html,body{width:915px;height:1200px;overflow:hidden}
body{position:relative;background:var(--page);font-family:"Open Sans",Arial,sans-serif;color:var(--ink)}
.abs{position:absolute}
ul{list-style:none}

.topbar{left:0;top:0;width:915px;height:30px;background:var(--bar);font-size:8px;color:#ddd;text-transform:uppercase}
.topbar .wishlist{left:254px;top:7px;width:108px;height:18px;background:#8a8a8a;border-radius:2px;color:#eee;text-transform:none;font-size:8px;text-align:center;line-height:18px}
.topbar .sep{left:370px;top:8px;width:1px;height:15px;background:#666}
.topbar .link{top:10px}
.topbar .flag{left:766px;top:11px;width:11px;height:7px;background:linear-gradient(#b22 0 50%,#fff 50% 60%,#b22 60%);}
.topbar .flag::before{content:"";position:absolute;left:0;top:0;width:5px;height:4px;background:#3b4d8a}
.topbar .caret{left:818px;top:13px;border:4px solid transparent;border-top-color:#777}

.header{left:0;top:30px;width:915px;height:112px;background:var(--white);border-bottom:1px solid #ddd}
.logo{left:84px;top:13px;width:113px;height:86px;border:1px solid #555;border-radius:6px;display:flex;align-items:center;justify-content:center;font-size:13px;font-weight:600;color:var(--ink)}
.social-top{top:30px;width:22px;height:22px;border-radius:2px;background:#2f6fa6}
.login{left:658px;top:66px;font-size:12px;letter-spacing:.5px}
.cart{left:790px;top:64px;width:32px;height:20px;background:#333}
.cart-count{left:814px;top:58px;width:14px;height:14px;border-radius:50%;background:#a11;color:#fff;font-size:9px;text-align:center;line-height:14px}

.nav{left:85px;top:152px;width:746px;height:23px;background:#f4f4f4;border-bottom:1px solid #ddd;font-size:9.5px}
.nav a{position:absolute;top:0;height:23px;line-height:23px;color:var(--ink);text-decoration:none}
.nav .home{left:0;width:57px;background:#111;color:#fff;padding-left:8px}
.nav .div{position:absolute;top:0;width:1px;height:23px;background:#ddd}
.nav .search{right:0;top:0;width:27px;height:23px;background:#9a9a9a}

.hero{left:85px;top:190px;width:746px;height:308px;background:linear-gradient(180deg,#cfd7d3 0%,#9aa37a 12%,#6f7b3c 30%,#3f5520 55%,#5b5426 75%,#9a7a3a 100%)}
.caption{left:102px;top:264px;width:279px;height:166px;background:rgba(15,15,15,.82);border-top:2px solid #fff;color:#fff;font-size:23px;font-weight:300;line-height:31px;padding:18px 0 0 14px;white-space:nowrap;letter-spacing:-.3px}
.caption b{font-weight:600}
.dot{top:437px;width:7px;height:7px;background:#111}

.content{left:85px;top:512px;width:746px;height:419px;background:var(--white);border-top:4px solid #d0d0d0}
.products-title{left:98px;top:524px;font-family:"Roboto Slab",Georgia,serif;font-size:17px}
.product-list{left:98px;top:551px;width:131px;font-size:9px;color:#333}
.product-list li{height:16.8px;line-height:16px;border-bottom:1px dashed #ccc;padding-left:15px;position:relative}
.product-list li::before{content:"→";position:absolute;left:1px;font-size:7px;color:var(--accent)}
.card{top:529px;width:125px;height:125px;background:#fff;border:1px solid #ccc;box-shadow:0 3px 4px rgba(0,0,0,.2);padding:5px}
.card .photo{width:100%;height:100%}
.price{top:668px;width:125px;text-align:center;font-size:20px;color:#333}
.btn{top:698px;height:16px;background:var(--btn);color:#fff;font-size:7px;text-align:center;line-height:16px}
.btn.add{background:#111}

.col-title{top:767px;font-size:14.5px;display:flex;align-items:center;gap:5px}
.col-text{font-size:8.7px;line-height:14.4px;color:#333;width:160px}
.more{font-size:9px;color:var(--accent)}
.video{left:287px;top:794px;width:162px;height:71px;background:linear-gradient(90deg,#2a1a10,#6a4a2a 50%,#3a2a18)}
.video .bar{position:absolute;left:0;bottom:0;width:100%;height:10px;background:#222}
.video .prog{position:absolute;left:0;bottom:10px;width:61px;height:2px;background:#c00}
.video .play{position:absolute;left:68px;top:14px;width:24px;height:24px;border-radius:50%;background:#eee}
.blog-thumb{left:476px;top:794px;width:44px;height:36px;background:linear-gradient(135deg,#3a1f10,#c98a3a)}

.footer{left:0;top:931px;width:915px;height:269px;background:var(--footer)}
.foot-line{left:0;top:973px;width:915px;height:1px;background:var(--footer-line)}
.foot-head{top:946px;font-size:11.5px;color:var(--footer-text)}
.foot-list{top:993px;font-size:9.5px;color:var(--footer-text)}
.foot-list li{height:16px;line-height:16px}
.foot-list li::before{content:"• ";font-size:7px}
.fsoc{top:996px;width:22px;height:22px;border-radius:2px}
.pay{top:1040px;width:24px;height:15px;background:#eee;border-radius:2px}
.copy{left:0;top:1179px;width:915px;text-align:center;font-size:9.5px;color:#ddd}
</style>
</head>
<body>

<div class="abs topbar">
  <div class="abs wishlist">My Wishlist (0 items)</div>
  <div class="abs sep"></div>
  <span class="abs link" style="left:389px">My Account</span>
  <span class="abs link" style="left:458px">Shopping Cart</span>
  <span class="abs link" style="left:540px">Checkout</span>
  <span class="abs link" style="left:671px">Choose Language:</span>
  <div class="abs flag"></div>
  <span class="abs link" style="left:783px;text-transform:none">English</span>
  <div class="abs caret"></div>
</div>

<div class="abs header">
  <div class="abs logo">Venlow Vaults</div>
  <div class="abs social-top" style="left:740px"></div>
  <div class="abs social-top" style="left:770px;background:#3b5998"></div>
  <div class="abs social-top" style="left:800px;background:#4aa8e0"></div>
  <div class="abs login">LOGIN &nbsp;&amp;&nbsp; REGISTER</div>
  <div class="abs cart">
    <svg width="32" height="20" viewBox="0 0 32 20"><path d="M9 6h2l2 7h8l2-5H12" fill="none" stroke="#fff" stroke-width="1.3"/><circle cx="14" cy="15.5" r="1.2" fill="#fff"/><circle cx="20" cy="15.5" r="1.2" fill="#fff"/></svg>
  </div>
  <div class="abs cart-count">0</div>
</div>

<nav class="abs nav">
  <a class="home">⌂ Home</a>
  <span class="div" style="left:57px"></span>
  <a style="left:79px">About Us</a>
  <span class="div" style="left:137px"></span>
  <a style="left:153px">Wines</a>
  <span class="div" style="left:198px"></span>
  <a style="left:213px">Store</a>
  <span class="div" style="left:254px"></span>
  <a style="left:270px">News</a>
  <span class="div" style="left:311px"></span>
  <a style="left:328px">Join the Venlow Family</a>
  <div class="abs search">
    <svg width="27" height="23" viewBox="0 0 27 23"><circle cx="12.5" cy="10.5" r="5" fill="none" stroke="#fff" stroke-width="2"/><path d="M16 14l4 4" stroke="#fff" stroke-width="2.4"/></svg>
  </div>
</nav>

<div class="abs hero" role="img" aria-label="Vineyard rows stretching across rolling fields under an evening sky"></div>
<div class="abs caption">We are <b>Fun, Reliable,</b><br><b>Trustworthy</b> &amp;<br><b>Guarantee</b> Everything<br>we Sell</div>
<div class="abs dot" style="left:104px;background:#fff"></div>
<div class="abs dot" style="left:115px"></div>
<div class="abs dot" style="left:126px"></div>

<div class="abs content"></div>
<h2 class="abs products-title">Our Products</h2>
<ul class="abs product-list">
  <li>Lorem Ipsum is</li><li>Simply dummy</li><li>Text of the</li><li>Printing and</li><li>Typesetting</li><li>Industry</li><li>Lorem Ipsum</li><li>Has been</li><li>The industry's</li>
</ul>

<div class="abs card" style="left:246px"><div class="photo" role="img" aria-label="Red wine glasses with bread and cheese" style="background:linear-gradient(160deg,#2a1a12,#7a4a2a 60%,#c9a070)"></div></div>
<div class="abs card" style="left:394px"><div class="photo" role="img" aria-label="White and red wine glasses with grapes and cheese" style="background:linear-gradient(160deg,#8a6a40,#c9a060 50%,#5a3a40)"></div></div>
<div class="abs card" style="left:543px"><div class="photo" role="img" aria-label="Glass of red wine against warm bokeh lights" style="background:radial-gradient(circle at 60% 60%,#6a1010,#3a2010 50%,#c08030)"></div></div>
<div class="abs card" style="left:692px"><div class="photo" role="img" aria-label="Red and white wine glasses with grape bunches" style="background:linear-gradient(160deg,#7a5a30,#b08a50 50%,#3a2030)"></div></div>

<div class="abs price" style="left:246px">$ 12.99</div>
<div class="abs price" style="left:394px">$ 12.99</div>
<div class="abs price" style="left:543px">$ 12.99</div>
<div class="abs price" style="left:692px">$ 12.99</div>

<div class="abs btn" style="left:251px;width:55px">DETAILS</div><div class="abs btn add" style="left:310px;width:56px">ADD TO CART</div>
<div class="abs btn" style="left:400px;width:55px">DETAILS</div><div class="abs btn add" style="left:458px;width:56px">ADD TO CART</div>
<div class="abs btn" style="left:548px;width:55px">DETAILS</div><div class="abs btn add" style="left:607px;width:56px">ADD TO CART</div>
<div class="abs btn" style="left:697px;width:55px">DETAILS</div><div class="abs btn add" style="left:756px;width:56px">ADD TO CART</div>

<div class="abs col-title" style="left:98px">
  <svg width="18" height="18" viewBox="0 0 18 18"><path d="M3 8h3v8H3zM6 9l3-6c1.5 0 2 1 1.5 3H15l-1 9H6" fill="none" stroke="#333" stroke-width="1.2"/></svg>Why Venlow
</div>
<div class="abs col-text" style="left:98px;top:803px">Lorem Ipsum is simply dummy text of the printing and typesetting industry. Lorem Ipsum has been the industry's standard dummy text ever since the 1500s.</div>
<div class="abs more" style="left:98px;top:880px">[ Read More . . . ]</div>

<div class="abs col-title" style="left:287px">
  <svg width="24" height="18" viewBox="0 0 24 18"><rect x="1" y="6" width="16" height="10" fill="none" stroke="#333" stroke-width="1.2"/><path d="M17 9l5-3v10l-5-3" fill="none" stroke="#333" stroke-width="1.2"/><circle cx="5" cy="3.5" r="2.5" fill="none" stroke="#333"/><circle cx="12" cy="3.5" r="2.5" fill="none" stroke="#333"/></svg>Video
</div>
<div class="abs video" role="img" aria-label="Video still of wine barrels in a cellar">
  <div class="prog"></div><div class="bar"></div>
  <div class="play"><svg width="24" height="24" viewBox="0 0 24 24"><path d="M10 7l7 5-7 5z" fill="#111"/></svg></div>
</div>
<div class="abs col-text" style="left:288px;top:870px">Lorem Ipsum is simply dummy text.</div>
<div class="abs more" style="left:288px;top:886px">[ Read More . . . ]</div>

<div class="abs col-title" style="left:476px">
  <svg width="16" height="18" viewBox="0 0 16 18"><rect x="2" y="1" width="12" height="16" fill="none" stroke="#333" stroke-width="1.2"/><path d="M4 5h8M4 8h8M4 11h8M4 14h6" stroke="#333"/></svg>Blog
</div>
<div class="abs blog-thumb" role="img" aria-label="Wine glass with cheese plate"></div>
<div class="abs" style="left:527px;top:791px;font-size:9.5px;color:var(--accent)">Une recherche</div>
<div class="abs col-text" style="left:476px;top:840px;color:#666;width:170px">Plusieurs variations de Lorem Ipsum peuvent être trouvées ici ou là, mais la majeure partie d'entre elles a été peuvent être</div>

<div class="abs col-title" style="left:659px">
  <svg width="17" height="17" viewBox="0 0 17 17"><circle cx="8.5" cy="8.5" r="7.5" fill="none" stroke="#8e1b1b" stroke-width="1.1"/><path d="M8.5 7v5.5M8.5 4.5v1" stroke="#8e1b1b" stroke-width="1.4"/></svg>Corporate Info
</div>
<div class="abs col-text" style="left:661px;top:803px">Lorem Ipsum is simply dummy text of the printing and typesetting industry. Lorem Ipsum has been the industry's standard dummy text ever since the 1500s.</div>
<div class="abs more" style="left:661px;top:880px">[ Read More . . . ]</div>

<footer class="abs footer"></footer>
<div class="abs foot-line"></div>
<div class="abs foot-head" style="left:97px">Customer Services</div>
<div class="abs foot-head" style="left:290px">Resources</div>
<div class="abs foot-head" style="left:469px">Corporate Info</div>
<div class="abs foot-head" style="left:634px">Social Media and Payment Method</div>

<ul class="abs foot-list" style="left:93px">
  <li>Shipping</li><li>Return Policy</li><li>Privacy Policy</li><li>Ordering &amp; Delivery</li><li>Checklist</li><li>Terms of Use</li><li>Terms of Sale</li><li>Contact Us</li><li>Environmental Policy</li>
</ul>
<ul class="abs foot-list" style="left:281px">
  <li>Product Articles</li><li>Learning Center</li><li>Help</li><li>Refer A Friend</li><li>Grapevale Blog</li><li>Room Scene Viewer</li><li>Site Map</li><li>FAQ</li><li>Customer Testimonials</li><li>Photo Gallery</li>
</ul>
<ul class="abs foot-list" style="left:465px">
  <li>About Grapevale.com</li><li>Careers</li><li>Affiliates</li>
</ul>

<div class="abs fsoc" style="left:634px;background:#2f6fa6"></div>
<div class="abs fsoc" style="left:664px;background:#3b5998"></div>
<div class="abs fsoc" style="left:694px;background:#4aa8e0"></div>
<div class="abs fsoc" style="left:725px;background:#e8782a"></div>
<div class="abs fsoc" style="left:757px;background:#e8662a"></div>
<div class="abs pay" style="left:634px"></div>
<div class="abs pay" style="left:663px"></div>
<div class="abs pay" style="left:692px"></div>
<div class="abs pay" style="left:722px;width:96px;height:20px;top:1038px;background:#4a4a4a"></div>

<div class="abs copy">© Copyrights 2013 &nbsp;Venlow Vaults. All rights Reserved</div>

</body>
</html>
```